Redesign of an educational Eye website for Medical Students and Healthcare professionals

www.corvantisportal.com is an educational resource, illustrated using high quality 3D animations, for undergraduate medical students and healthcare professionals to learn about the anatomy of the human eye and associated common eye disorders.

The website was originally developed (using a Joomla template) a couple of years ago and we now want to update the brand and design of the site. Example content and animations can be found at https://www.corvantisportal.com/overview or https://www.corvantisportal.com/ocular-anatomy/orbital-anatomy

We would like a new logo and home page design (to include new colour palette, fonts and updated overall design).

The attached PowerPoint contains an example layout of the revised components we want to appear on the new Home page. We plan to have a hero panel at the top of page playing a short video of some of the animations. Similar to how this site works (www.zembri.uk.com).

We want the new site to feel Professional, Modern and Clean and simple.

Target Market(s)

Undergraduate medical students and Healthcare Professionals

Industry/Entity Type

Medical

Logo Text

Corvantis Portal

Number of Pages Required

1 page

Font styles to use
Sans Serif

Colors

Designer to choose colors to be used in the design.

```html
<!DOCTYPE html>
<html lang="en">
<head>
<meta charset="utf-8">
<title>Corvantis Portal – Learn Faster and Smarter</title>
<link href="https://fonts.googleapis.com/css2?family=Roboto:wght@300;400;500;700&family=Montserrat:wght@400;500;600&family=Playfair+Display:wght@500&display=swap" rel="stylesheet">
<style>
:root{
  --brand:#3b4ba8;
  --brand-dark:#2c3a8f;
  --trial:#6c7cc9;
  --green:#5cae2e;
  --ink:#333;
  --muted:#777;
  --grey-bg:#f1f1f1;
  --line:#29a8e0;
  --footer:#1f1f1f;
  --white:#fff;
}
*{box-sizing:border-box;margin:0;padding:0}
html,body{width:1200px;height:4891px;overflow:hidden}
body{font-family:"Roboto",sans-serif;color:var(--ink);background:var(--white);position:relative}
section,header,footer{position:absolute;left:0;width:1200px}
.ph{display:block}
h2.section-title{font-family:"Montserrat",sans-serif;font-weight:500;text-align:center;color:#222}

/* header */
.site-header{top:0;height:92px;background:var(--white);display:flex;align-items:center;justify-content:space-between;padding:0 80px}
.brand-name{font-family:"Roboto",sans-serif;font-weight:400;font-size:36px;color:var(--brand);display:flex;align-items:center;gap:12px}
.brand-name i{width:12px;height:12px;border-radius:50%;background:var(--brand);display:block}
.sign-in{background:var(--brand);color:#fff;font-size:17px;font-weight:500;padding:10px 22px;border-radius:6px;display:flex;align-items:center;gap:10px}

/* hero */
.hero{top:92px;height:511px;background:linear-gradient(100deg,#0a1a3a 0%,#123a6e 22%,#d8661a 30%,#f28a2e 35%,#0f2f5e 48%,#0b1f45 75%,#163d72 100%)}
.hero-copy{position:absolute;left:650px;top:110px;width:460px;color:#fff;text-align:center}
.hero-copy h1{font-family:"Playfair Display",serif;font-weight:500;font-size:31px;letter-spacing:1px;margin-bottom:18px}
.hero-copy p{font-size:17px;line-height:1.3;margin-bottom:26px}
.hero-btn{display:block;width:270px;margin:0 auto 16px;background:var(--brand);color:#fff;font-size:16px;font-weight:500;padding:13px 0;border-radius:5px}
.hero-btn.wide{width:310px}

/* trusted */
.trusted{top:603px;height:262px}
.trusted h2{position:absolute;top:30px;width:100%;font-size:28px}
.badges{position:absolute;top:110px;left:115px;right:115px;display:flex;justify-content:space-between}
.badge{width:110px;height:80px;border-radius:8px;background:#e4e4e4}

/* why */
.why{top:865px;height:895px;background:var(--grey-bg)}
.why h2{position:absolute;top:40px;width:100%;font-size:36px}
.feature-text{position:absolute;width:480px}
.feature-text h3{font-family:"Montserrat",sans-serif;font-weight:500;font-size:28px;color:#222;margin-bottom:8px}
.feature-text p{font-size:17px;color:var(--muted);line-height:1.55}
.credible-text{left:92px;top:180px}
.credible-img{position:absolute;left:600px;top:113px;width:535px;height:365px;background:linear-gradient(135deg,#f3e6de,#c98f78 50%,#7a5a4a)}
.visual-img{position:absolute;left:65px;top:478px;width:535px;height:368px;background:linear-gradient(160deg,#8c5f45,#c48c6c 50%,#6a4434)}
.visual-text{left:635px;top:540px}

/* modules */
.modules{top:1760px;height:532px}
.modules h2{position:absolute;top:30px;width:100%;font-size:36px}
.cards{position:absolute;top:98px;left:75px;display:flex;gap:26px}
.module-card{width:332px;height:378px;background:#fff;border:1px solid #e3e3e3}
.module-img{height:200px;background:linear-gradient(180deg,#c99a84,#8d5c48)}
.module-img.m2{background:linear-gradient(180deg,#6b4530,#3d2518)}
.module-img.m3{background:linear-gradient(180deg,#d7b8a8,#9a7464)}
.module-body{padding:18px 14px}
.module-body h3{font-family:"Montserrat",sans-serif;font-weight:500;font-size:20px;margin-bottom:10px}
.module-body p{font-size:13px;color:var(--muted);line-height:1.45;margin-bottom:14px}
.read-more{font-size:13px;font-weight:700;color:#222}

/* team */
.team{top:2292px;height:495px;background:var(--grey-bg)}
.team h2{position:absolute;top:30px;width:100%;font-size:36px}
.members{position:absolute;top:94px;left:75px;display:flex;gap:30px}
.member{width:240px;height:362px;background:#fff}
.member-photo{height:264px;background:linear-gradient(180deg,#fafafa,#d9d0c8);border-bottom:4px solid var(--line)}
.member h3{text-align:center;font-weight:500;font-size:17px;margin-top:26px}
.member span{display:block;text-align:center;font-size:11px;color:#999;font-style:italic;margin-top:6px}

/* testimonial */
.testimonial{top:2787px;height:353px}
.testimonial h2{position:absolute;top:40px;width:100%;font-size:28px}
.quote-photo{position:absolute;left:104px;top:124px;width:176px;height:176px;background:linear-gradient(180deg,#b8b8b8,#3a3d48)}
.quote{position:absolute;left:300px;top:128px;width:790px}
.quote h3{font-family:"Montserrat",sans-serif;font-weight:400;font-size:22px;margin-bottom:10px}
.quote strong{display:block;font-size:14px;margin-bottom:8px}
.quote p{font-size:14px;color:#555;line-height:1.6}

/* trial */
.trial{top:3140px;height:707px;background:var(--trial);color:#fff;text-align:center}
.trial h2{position:absolute;top:62px;width:100%;font-size:34px;color:#fff}
.trial .sub{position:absolute;top:118px;width:100%;font-size:18px;color:#e6e9f7}
.trial-btn{position:absolute;left:450px;top:162px;width:200px;height:62px;background:var(--green);color:#fff;font-weight:500;font-size:17px;line-height:62px;border-radius:3px}
.video{position:absolute;left:264px;top:267px;width:584px;height:385px;border-radius:10px;background:linear-gradient(180deg,#6a4a3c,#a6745c 40%,#c99a7e)}
.play{position:absolute;left:262px;top:162px}

/* charity */
.charity{top:3847px;height:179px;text-align:center}
.charity h2{position:absolute;top:40px;width:100%;font-size:34px}
.charity p{position:absolute;top:98px;left:160px;width:880px;font-size:15px;color:#444;line-height:1.5}
.charity-band{top:4026px;height:424px;background:linear-gradient(90deg,#3a2a26,#8a7062 30%,#3a6d9c 55%,#1c3b62 75%,#6b8fb5)}

/* footer */
.site-footer{top:4450px;height:391px;background:var(--footer);color:#fff}
.fcol{position:absolute}
.fcol h4{font-size:13px;font-weight:700;letter-spacing:.5px;margin-bottom:14px}
.fcol li{list-style:none;font-size:14px;margin-bottom:10px;display:flex;align-items:center;gap:8px}
.fcol li::before{content:"";width:5px;height:5px;border-radius:50%;background:var(--line)}
.newsletter p{font-size:14px;margin-bottom:14px}
.subscribe{display:flex;gap:10px}
.subscribe span{width:280px;height:32px;background:#fff;border-radius:4px}
.subscribe b{background:var(--brand);font-weight:400;font-size:14px;padding:7px 16px;border-radius:4px}
.footer-brand{position:absolute;left:860px;top:80px;font-size:38px;color:#9a9a9a}
.copyright{top:4841px;height:50px;background:var(--brand);color:#fff;font-size:14px;text-align:center;line-height:50px}
</style>
</head>
<body>

<header class="site-header">
  <div class="brand-name"><i></i>Corvantis Portal</div>
  <div class="sign-in">Sign In
    <svg width="18" height="18" viewBox="0 0 18 18" fill="none" stroke="#fff" stroke-width="2"><path d="M7 3h8v12H7"/><path d="M2 9h9M8 6l3 3-3 3"/></svg>
  </div>
</header>

<section class="hero">
  <div class="ph" role="img" aria-label="Close-up of a human eye with orange iris on a digital blue background" style="position:absolute;inset:0"></div>
  <div class="hero-copy">
    <h1>LEARN FASTER AND SMARTER</h1>
    <p>Corvantis Portal helps undergraduates and healthcare professionals to learn or update their knowledge of the clinically relevant anatomy, ophthalmic examination techniques and common eye disorders of the human eye.</p>
    <span class="hero-btn">Undergraduates – Learn more</span>
    <span class="hero-btn wide">Healthcare Professionals – Learn more</span>
  </div>
</section>

<section class="trusted">
  <h2 class="section-title">Trusted Across The World</h2>
  <div class="badges">
    <div class="badge"></div><div class="badge"></div><div class="badge"></div>
    <div class="badge"></div><div class="badge"></div><div class="badge"></div>
  </div>
</section>

<section class="why">
  <h2 class="section-title">Why Corvantis Portal?</h2>
  <div class="feature-text credible-text">
    <h3>CREDIBLE</h3>
    <p>Written and illustrated by experienced Consultant Ophthalmologists.<br>-<br>Designed and supported by experts - Focused on constructive feedback, insights and action - Continuously improved by 1000+ innovative companies</p>
  </div>
  <div class="credible-img" role="img" aria-label="Eye drops being applied to an open eye"></div>
  <div class="visual-img" role="img" aria-label="3D animated rendering of a man's face"></div>
  <div class="feature-text visual-text">
    <h3>VISUAL</h3>
    <p>Key concepts brought to life using stunning 3D animations<br><br>- Helps you build a comprehensive feedback strategy - Gives your whole organization real-time, valuable insights - Grows with your increasing needs</p>
  </div>
</section>

<section class="modules">
  <h2 class="section-title">Training Modules</h2>
  <div class="cards">
    <article class="module-card">
      <div class="module-img" role="img" aria-label="Close-up of a red irritated eye"></div>
      <div class="module-body"><h3>Core Principales</h3><p>Lorem ipsum dolor sit amet, consectetur adipis elit sed do eiusmod tempor incidunt labore et dolore magna aliqua.</p><span class="read-more">Read More</span></div>
    </article>
    <article class="module-card">
      <div class="module-img m2" role="img" aria-label="Close-up of a pair of dark eyes"></div>
      <div class="module-body"><h3>Ophthalmology Practice</h3><p>Lorem ipsum dolor sit amet, consectetur adipis elit sed do eiusmod tempor incidunt labore et dolore magna aliqua.</p><span class="read-more">Read More</span></div>
    </article>
    <article class="module-card">
      <div class="module-img m3" role="img" aria-label="Close-up of a pale eye"></div>
      <div class="module-body"><h3>AN other</h3><p>Lorem ipsum dolor sit amet, consectetur adipis elit sed do eiusmod tempor incidunt labore et dolore magna aliqua.</p><span class="read-more">Read More</span></div>
    </article>
  </div>
</section>

<section class="team">
  <h2 class="section-title">Meet the team</h2>
  <div class="members">
    <div class="member"><div class="member-photo" role="img" aria-label="Portrait of team member"></div><h3>Marina Colby</h3><span>Lead Advisor</span></div>
    <div class="member"><div class="member-photo" role="img" aria-label="Portrait of team member"></div><h3>Stefan Orwell</h3><span>Lead Advisor</span></div>
    <div class="member"><div class="member-photo" role="img" aria-label="Portrait of team member"></div><h3>Wilfred Arden</h3><span>Lead Advisor</span></div>
    <div class="member"><div class="member-photo" role="img" aria-label="Portrait of team member"></div><h3>Brandon Tilley</h3><span>Lead Advisor</span></div>
  </div>
</section>

<section class="testimonial">
  <h2 class="section-title">What are people saying About Corvantis Portal?</h2>
  <div class="quote-photo" role="img" aria-label="Portrait of consultant ophthalmologist"></div>
  <div class="quote">
    <h3>Mr Julian Fenwick MB ChB FRCOphth</h3>
    <strong>Consultant Ophthalmologist and Head of the School of Ophthalmology, Northvale Deanery HENV</strong>
    <p>What sets this website apart are the superb 3D animations which enhance the accompanying text more effectively than clinical videos or photographs. I would whole heartedly recommend it to medical students, optometrists, GPs, casualty doctors and ophthalmic nurse practitioners, both as an introduction to ophthalmology but also to refresh their knowledge of core ophthalmic examination techniques and conditions.</p>
  </div>
</section>

<section class="trial">
  <h2 class="section-title">Want to Try Corvantis Portal for Free ?</h2>
  <p class="sub">No Credit card details required.It's completely free for 3 days.</p>
  <span class="trial-btn">Start Free Trial</span>
  <div class="video" role="img" aria-label="Video still of an animated eye examination">
    <svg class="play" width="60" height="60" viewBox="0 0 60 60"><circle cx="30" cy="30" r="30" fill="#fff"/><path d="M24 18l18 12-18 12z" fill="#333"/></svg>
  </div>
</section>

<section class="charity">
  <h2 class="section-title">We give 10% of our profile to charity</h2>
  <p>We believe it is important to give something back so from 2018 we will donate 10% of every subscription to a selected charity somewhere in the world which works to help prevent sight loss and treat eye diseases.</p>
</section>
<section class="charity-band" role="img" aria-label="Eye close-up with a digital scanning overlay"></section>

<footer class="site-footer">
  <div class="fcol" style="left:92px;top:40px"><h4>COMMUNITY</h4><ul><li>Friendloop</li><li>Chirpline</li><li>Workweave</li></ul></div>
  <div class="fcol newsletter" style="left:404px;top:40px"><h4>NEWSLETTER</h4><p>Subscribe</p><div class="subscribe"><span></span><b>Subscribe</b></div></div>
  <div class="footer-brand">Corvantis Portal</div>
  <div class="fcol" style="left:92px;top:212px"><h4>PRODUCTS</h4><ul><li>Employee Engagement</li><li>Employee Effectiveness</li><li>Employee Experience</li><li>Plants &amp; Pricing</li></ul></div>
  <div class="fcol" style="left:410px;top:212px"><h4>RESOURCES</h4><ul><li>Employee Engagement</li><li>Employee Effectiveness</li><li>Employee Experience</li><li>Plants &amp; Pricing</li></ul></div>
  <div class="fcol" style="left:688px;top:212px"><h4>COMPANY</h4><ul><li>Our Story</li><li>Customers</li><li>Carees</li></ul></div>
  <div class="fcol" style="left:882px;top:212px"><h4>CONTACT US</h4><ul><li>Email Sales</li><li>Email Support</li></ul></div>
</footer>
<div class="copyright" style="position:absolute;left:0;width:1200px">Copyright © 2018. Lumenvale Limited.</div>

</body>
</html>
```